New business card design needed for Diesel Fitting (Mechanical) Company

We need a new business card for our company called "Granite Valley Engineering" that showcases our logo and business details.
Target Market(s)
Owners of all makes and models of vehicles, trucks, plant and machinery.
Industry/Entity Type
Mechanical
Contact Information for Business Card
The business card details need to include the following: Owners/Directors: Trevor & Marisol Dunn-Calloway ABN: 47 913 206 781 Address: 561 Beaumont Street IRONBARK FLATS QLD 4735 Postal Address: PO Box 8716 IRONBARK FLATS QLD 4735 Website: www.gvengineering.com.au Phone: 4732 9185 Mobile: 0491 375 806 Emails: sales@gvengineering.com.au; admin@gvengineering.com.au; accounts@gvengineering.com.au; parts@gvengineering.com.au; office@gvengineering.com.au, reception@gvengineering.com.au
Look and feel

```html
<!DOCTYPE html>
<html lang="en">
<head>
<meta charset="utf-8">
<title>Granite Valley Engineering – Business Card</title>
<link href="https://fonts.googleapis.com/css2?family=Questrial&display=swap" rel="stylesheet">
<style>
  :root {
    --bg: #2a2a2a;
    --card: #0d0d0d;
    --orange: #f47a20;
    --white: #f2f2f2;
    --silver: #d9d9d9;
    --rule: #555555;
  }
  * { box-sizing: border-box; margin: 0; padding: 0; }
  html, body {
    width: 1200px; height: 900px; overflow: hidden;
    background: var(--bg);
    font-family: "Questrial", "Century Gothic", sans-serif;
  }
  .canvas {
    width: 1200px; height: 900px;
    display: flex; flex-direction: column; align-items: center; justify-content: center;
    gap: 54px;
  }
  .card {
    width: 560px; height: 343px;
    background: var(--card);
    border-radius: 18px;
    position: relative;
    overflow: hidden;
  }
  /* Front */
  .card-front { display: flex; padding: 32px 26px 30px 30px; }
  .front-left { width: 212px; flex: none; display: flex; flex-direction: column; justify-content: space-between; }
  .brand { display: flex; align-items: center; gap: 12px; margin-top: 34px; }
  .brand-dot { width: 22px; height: 22px; border-radius: 50%; background: var(--orange); flex: none; }
  .brand-name { color: var(--orange); font-size: 23px; line-height: 1.15; }
  .addresses { list-style: none; display: flex; flex-direction: column; gap: 14px; }
  .addresses li { display: flex; gap: 8px; color: var(--white); font-size: 14px; line-height: 1.35; }
  .addresses .icon { margin-top: 2px; }
  .divider { width: 1px; flex: none; background: var(--rule); margin: 0 18px; }
  .front-right { flex: 1; min-width: 0; display: flex; flex-direction: column; }
  .owners { color: var(--orange); font-size: 15.5px; white-space: nowrap; }
  .role, .abn { color: var(--white); font-size: 13.5px; margin-top: 4px; white-space: nowrap; }
  .abn .label { color: var(--orange); }
  .phones, .emails { list-style: none; }
  .phones { margin-top: 16px; }
  .phones li, .emails li { display: flex; align-items: center; gap: 8px; color: var(--white); font-size: 13.5px; line-height: 1.5; white-space: nowrap; }
  .emails { margin-top: 12px; }
  .emails li { font-size: 13px; line-height: 1.6; }
  .icon { width: 13px; height: 13px; flex: none; fill: var(--orange); }
  /* Back */
  .card-back { display: flex; flex-direction: column; align-items: center; justify-content: center; gap: 40px; }
  .back-brand { display: flex; align-items: center; gap: 14px; }
  .back-brand .brand-dot { background: var(--silver); width: 26px; height: 26px; }
  .back-brand .brand-name { color: var(--silver); font-size: 30px; }
  .website { color: var(--white); font-size: 14px; letter-spacing: 2px; }
</style>
</head>
<body>
<main class="canvas">
  <section class="card card-front">
    <div class="front-left">
      <div class="brand">
        <span class="brand-dot"></span>
        <span class="brand-name">Granite Valley Engineering</span>
      </div>
      <ul class="addresses">
        <li><svg class="icon" viewBox="0 0 12 12"><path d="M6 0a4 4 0 0 0-4 4c0 3 4 8 4 8s4-5 4-8a4 4 0 0 0-4-4zm0 5.5A1.5 1.5 0 1 1 6 2.5a1.5 1.5 0 0 1 0 3z"/></svg><span>561 Beaumont Street<br>Ironbark Flats QLD 4735</span></li>
        <li><svg class="icon" viewBox="0 0 12 12"><path d="M6 0a4 4 0 0 0-4 4c0 3 4 8 4 8s4-5 4-8a4 4 0 0 0-4-4zm0 5.5A1.5 1.5 0 1 1 6 2.5a1.5 1.5 0 0 1 0 3z"/></svg><span>PO Box 8716 Ironbark<br>Flats QLD 4735</span></li>
      </ul>
    </div>
    <div class="divider"></div>
    <div class="front-right">
      <p class="owners">Trevor &amp; Marisol Dunn-Calloway</p>
      <p class="role">Owners/Directors</p>
      <p class="abn"><span class="label">ABN:</span> 47 913 206 781</p>
      <ul class="phones">
        <li><svg class="icon" viewBox="0 0 12 12"><path d="M2.5 0.5l2 2.5-1.2 1.3c.7 1.6 2 2.9 3.6 3.6L8.2 6.7l2.5 2-1 2.3C5 10.8 1.2 7 1 2.3z"/></svg>4732 9185</li>
        <li><svg class="icon" viewBox="0 0 12 12"><path d="M3 0h6a1 1 0 0 1 1 1v10a1 1 0 0 1-1 1H3a1 1 0 0 1-1-1V1a1 1 0 0 1 1-1zm0 1.5v7.5h6V1.5zM6 9.8a.7.7 0 1 0 0 1.4.7.7 0 0 0 0-1.4z"/></svg>0491 375 806</li>
      </ul>
      <ul class="emails">
        <li><svg class="icon" viewBox="0 0 12 12"><path d="M0 2h12v8H0zm1 1v.4l5 3.3 5-3.3V3z"/></svg>sales@gvengineering.com.au</li>
        <li><svg class="icon" viewBox="0 0 12 12"><path d="M0 2h12v8H0zm1 1v.4l5 3.3 5-3.3V3z"/></svg>admin@gvengineering.com.au</li>
        <li><svg class="icon" viewBox="0 0 12 12"><path d="M0 2h12v8H0zm1 1v.4l5 3.3 5-3.3V3z"/></svg>accounts@gvengineering.com.au</li>
        <li><svg class="icon" viewBox="0 0 12 12"><path d="M0 2h12v8H0zm1 1v.4l5 3.3 5-3.3V3z"/></svg>parts@gvengineering.com.au</li>
        <li><svg class="icon" viewBox="0 0 12 12"><path d="M0 2h12v8H0zm1 1v.4l5 3.3 5-3.3V3z"/></svg>office@gvengineering.com.au</li>
        <li><svg class="icon" viewBox="0 0 12 12"><path d="M0 2h12v8H0zm1 1v.4l5 3.3 5-3.3V3z"/></svg>reception@gvengineering.com.au</li>
      </ul>
    </div>
  </section>

  <section class="card card-back">
    <div class="back-brand">
      <span class="brand-dot"></span>
      <span class="brand-name">Granite Valley Engineering</span>
    </div>
    <p class="website">www.gvengineering.com.au</p>
  </section>
</main>
</body>
</html>
```